Contractor Plan "B"/Getting Screwed?/Something Useful

We are sending out a series of postcards to a group of local contractors.

The first in the series is: Plan B: Pink Bubble Wrap. Plan A is to buy insurance from my agency. This will be printed, front and back on card stock. We will then glue a piece of bubble wrap to the card and place it in an envelope for delivery.

The second card will be along the same lines but will ask if the client is getting screwed by his current Insurance Company. We will glue a screw in the middle of the card and place the card in an envelope for delivery. On the bottom of we might tell them to call us to get unscrewed.

The third card will follow those lines but say something like: We sent you bubble wrap for your Plan B and you didn't call. Then we sent you something funny but you didn't call. We decided to send you something useful so you might call now! With this card, we are going to send a carpenter pencil.

I am attaching a rough outline of my sketch design for the first card so you will have basic information we will need such as phone number and coverages we offer. If you feel like there is too much info for the size of the card, we can leave some off. I just want the phone to ring! Also, feel free to adjust the wording to make it work better...creative design is not my strong suit!!

I would like for all three cards to be designed. Each can have the same backside. Also, please keep in mind, this is not a postcard so you don't have to leave the blanks on the back for addressing. Each will be mailed in an envelope.

I have also uploaded my logo file as we have recently redone the logo.

Here is more guidance on the project: The cards are going to be 10 cm wide and 23 cm tall. I have added more wording in the brief. Also, I attached a word doc with a good idea of what to use for wording. Basically I want the following idea: Card 1: At top of card - Plan B: Pink Bubble Wrap Below the bubble wrap - Plan A: Call us so you don't have to use Pink Bubble Wrap Card 2: At top of card - Getting Screwed? Is your current agent taking you for granted? Below the area where we are going to glue a screw - Get unscrewed, Call us! Card 3: At top of card - We have the sharpest pencil in town! We will leave space for a carpenter pencil to be attached tot he card. On the other side of the open space - Call us today for the best rates on your insurance!

Please review the attached word doc for an idea of what to put on the back of the card. To be clear, we need three designs for the front of the card and can probably use just one design for the back of all three. If you think we need to have a different design for the back of each, I would like to see your ideas. Thank you for your hard work on these!

Reason: Hi, I am extending the time as I am expecting a few more submissions. Thank you!

Target Market(s)

We are targeting both contractors and truckers with this campaign.

Industry/Entity Type

Insurance

Requirements
Must have
• Clever wording. It needs to be a call to action and doesn't need to have too many specifics.

We also have to have space in the middle to glue the bubble wrap on the first card, the screw in the second and attach the pencil in the third.

```html
<!DOCTYPE html>
<html lang="en">
<head>
<meta charset="utf-8">
<title>Northline Contractor Card Series</title>
<link href="https://fonts.googleapis.com/css2?family=Bebas+Neue&family=Oswald:wght@300;600&display=swap" rel="stylesheet">
<style>
  :root {
    --stage: #333333;
    --card: #e3e3e3;
    --card-light: #ececec;
    --card-shade: #d4d4d4;
    --brand-ink: #484848;
    --blue: #1b93e8;
    --pink: #e52d9f;
    --orange: #f47a12;
    --orange-ink: #ef7b1a;
    --green: #45a000;
    --green-ink: #4a9a12;
    --lime: #86e01e;
  }
  * { box-sizing: border-box; margin: 0; padding: 0; }
  html, body { width: 1200px; height: 1000px; overflow: hidden; background: var(--stage); }
  .stage { position: relative; width: 1200px; height: 1000px; }
  .card {
    position: absolute; top: 89px; width: 362px; height: 832px;
    background: var(--card); overflow: hidden; text-align: center;
  }
  .card--bubble { left: 48px; }
  .card--screw { left: 420px; }
  .card--pencil { left: 794px; }
  .card__shapes { position: absolute; inset: 0; width: 362px; height: 832px; }
  .card > .brand, .card > .text { position: absolute; left: 0; right: 0; }

  .brand { top: 18px; }
  .brand__name {
    font-family: "Bebas Neue", sans-serif; font-size: 62px; line-height: 1;
    color: var(--brand-ink); letter-spacing: 3px;
  }
  .brand__tag {
    font-family: "Bebas Neue", sans-serif; font-size: 15px; line-height: 1;
    color: var(--brand-ink); letter-spacing: 1px; margin-top: 2px;
  }

  .headline { font-family: "Oswald", sans-serif; font-weight: 300; text-transform: uppercase; }
  .headline b { font-weight: 600; }
  .underline { text-decoration: underline; text-underline-offset: 5px; text-decoration-thickness: 1.5px; }

  /* card 1 */
  .plan-b { top: 124px; font-family: "Bebas Neue", sans-serif; font-size: 32px; color: var(--blue); letter-spacing: 0.5px; }
  .plan-b .pink { color: var(--pink); }
  .plan-a { top: 478px; font-family: "Bebas Neue", sans-serif; color: var(--blue); }
  .plan-a__title { font-size: 58px; line-height: 1; display: inline-block; border-bottom: 2px solid var(--blue); padding-bottom: 2px; letter-spacing: 1px; }
  .plan-a__body { font-size: 33px; line-height: 48px; margin-top: 6px; }

  /* card 2 */
  .screwed-title { top: 114px; font-size: 30px; letter-spacing: 2px; color: var(--orange-ink); }
  .screwed-question { top: 204px; font-size: 21px; line-height: 31px; letter-spacing: 1px; color: var(--orange-ink); }
  .unscrewed { top: 632px; color: var(--orange-ink); }
  .unscrewed__lead { font-size: 38px; letter-spacing: 3px; line-height: 1.1; }
  .unscrewed__cta { font-size: 52px; letter-spacing: 3px; line-height: 1.15; }

  /* card 3 */
  .follow-up { top: 148px; font-size: 21px; line-height: 53.5px; letter-spacing: 1px; color: var(--green-ink); }
</style>
</head>
<body>
<main class="stage">

  <section class="card card--bubble">
    <svg class="card__shapes" viewBox="0 0 362 832" aria-hidden="true">
      <polygon points="0,170 362,110 362,832 0,832" fill="var(--card-light)"/>
      <polygon points="0,600 362,540 362,832 0,832" fill="var(--card-shade)"/>
      <polygon points="305,660 362,540 362,740" fill="#cfcfcf"/>
      <line x1="10" y1="47" x2="95" y2="47" stroke="var(--blue)" stroke-width="2.5"/>
      <line x1="267" y1="47" x2="352" y2="47" stroke="var(--blue)" stroke-width="2.5"/>
      <polygon points="0,262 362,207 362,367 0,487" fill="var(--blue)"/>
      <defs>
        <linearGradient id="bubbleTone" x1="0" y1="0" x2="1" y2="1">
          <stop offset="0" stop-color="#e07f99"/>
          <stop offset="0.5" stop-color="#d45e7f"/>
          <stop offset="1" stop-color="#c9486c"/>
        </linearGradient>
      </defs>
      <polygon role="img" aria-label="Sheet of pink bubble wrap" points="0,269 362,214 362,360 0,480" fill="url(#bubbleTone)"/>
    </svg>
    <div class="brand">
      <div class="brand__name">NORTHLINE</div>
      <div class="brand__tag">INSURANCE GROUP</div>
    </div>
    <p class="text plan-b"><span class="underline">PLAN B: <span class="pink">PINK</span> BUBBLE WRAP</span></p>
    <div class="text plan-a">
      <div class="plan-a__title">PLAN A:</div>
      <p class="plan-a__body">CALL US SO<br>YOU DON'T HAVE<br>TO USE PINK<br>BUBBLE WRAP.</p>
    </div>
  </section>

  <section class="card card--screw">
    <svg class="card__shapes" viewBox="0 0 362 832" aria-hidden="true">
      <polygon points="0,190 362,110 362,832 0,832" fill="var(--card-light)"/>
      <polygon points="0,590 362,550 362,832 0,832" fill="var(--card-shade)"/>
      <line x1="10" y1="47" x2="95" y2="47" stroke="var(--orange)" stroke-width="2.5"/>
      <line x1="267" y1="47" x2="352" y2="47" stroke="var(--orange)" stroke-width="2.5"/>
      <polygon role="img" aria-label="Two wood screws on an orange band" points="0,313 362,345 362,548 0,588" fill="var(--orange)"/>
    </svg>
    <div class="brand">
      <div class="brand__name">NORTHLINE</div>
      <div class="brand__tag">INSURANCE GROUP</div>
    </div>
    <p class="text headline screwed-title"><span class="underline">GETTING <b>SCREWED?</b></span></p>
    <p class="text headline screwed-question">IS YOUR <b>CURRENT INSURANCE<br>COMPANY</b> TAKING YOU FOR <b>GRANTED</b>?</p>
    <div class="text headline unscrewed">
      <p class="unscrewed__lead">GET UNSCREWED,</p>
      <p class="unscrewed__cta"><b class="underline">CALL US!</b></p>
    </div>
  </section>

  <section class="card card--pencil">
    <svg class="card__shapes" viewBox="0 0 362 832" aria-hidden="true">
      <polygon points="0,160 362,110 362,832 0,832" fill="var(--card-light)"/>
      <polygon points="0,520 362,470 362,832 0,832" fill="var(--card-shade)"/>
      <line x1="10" y1="47" x2="95" y2="47" stroke="var(--lime)" stroke-width="2.5"/>
      <line x1="267" y1="47" x2="352" y2="47" stroke="var(--lime)" stroke-width="2.5"/>
      <polygon role="img" aria-label="Carpenter pencil on a green band" points="0,538 362,578 362,755 0,780" fill="var(--green)"/>
    </svg>
    <div class="brand">
      <div class="brand__name">NORTHLINE</div>
      <div class="brand__tag">INSURANCE GROUP</div>
    </div>
    <p class="text headline follow-up">
      WE SENT SOME <b>BUBBLE WRAP</b>,<br>
      YOU DIDN'T CALL.<br>
      WE OFFERED TO <b>UNSCREW</b> YOU<br>
      AND WE DIDN'T HEAR BACK.<br>
      NOW, WE ARE SENDING SOMETHING<br>
      <span class="underline"><b>USEFUL</b> HOPING YOU WILL CALL!</span>
    </p>
  </section>

</main>
</body>
</html>
```